Professional Talent Needed Yesterday! Mesa Kinfolk Vineyard needs 2 wine labels-both front & back

Our vineyard, QT HOLLOWPATH WINE LLC, has associated with a "Custom Crush" winery to make our wine. Our first red and white blends are finally ready to be labeled, bottled & sold (we hope)

We now need to quickly create front and back (maybe wraparound?) labels - & then electronically provide them to our Custom Crush winery, DRAVENMOOR WINE COMPANY.

The front label can be completely creative but the back label needs to contain both some narrative description of the wine, but also government-required disclosure information (listed below) As required by federal law, DRAVENMOOR WINE COMPANY must submit both the front and the back label "prototypes" to obtain "official" permission to use - prior to printing any labels.

Did I say, "time is of the essence"...we just completed our logo through
logofable & they provided this link & a copy of all of our files...

Thank you for professional help!

Juna
(Juna Welt Imrie)
QTHOLLOWPATH WINE LLC
weltimriewine@vinomail.example
928-461-3092

Target Market(s)

intergenerational wine drinkers: "aficionados" not necessarily "connoisseurs""-both millennials as well their grandparents-those desiring to expand their wine experience to the high desert terroir in Arizona!

Font styles to use
Serif
Sans Serif
Script

Requirements
Must have
• - Modern design-elegant, bold, clean and easy to read font...
- Incorporate our new brand logo (or some variation of it) Our logo includes a "Southwest Mission Arch" type shape...
- All of the required governmental disclosures- see uploaded attachment
Nice to have
• -Most of the label elements for the red blend and the white blend are the same- both for the front and back labels- so the design/layout can be almost the same for each blend or they can be somewhat differentiated with any variation you believe would be complementary to each label-maybe inverse ideas (?)
- complete freedom with layout on both front & back label (attachments for required narrative & disclosure statements only)
- any "standard "size of labels for flexibility and ease of printing- shape/color of wine bottles still to be determined
- Our tag line and our names in script font

```html
<!DOCTYPE html>
<html lang="en">
<head>
<meta charset="utf-8">
<title>K&amp;W Red – Front and Back Labels</title>
<link rel="stylesheet" href="https://fonts.googleapis.com/css2?family=DM+Serif+Display&family=Playfair+Display:wght@400;700&family=Pinyon+Script&family=Open+Sans:wght@300;400;600;700&display=swap">
<style>
  :root {
    --canvas: #efeff0;
    --label-red: #8f181c;
    --stain: #5e0e12;
    --ink-light: #ffffff;
    --ink-dark: #2a0708;
  }
  * { box-sizing: border-box; margin: 0; padding: 0; }
  html, body { width: 1200px; height: 800px; overflow: hidden; }
  body { background: var(--canvas); position: relative; }

  .label {
    position: absolute;
    top: 86px;
    width: 470px;
    height: 627px;
    background: var(--label-red);
    color: var(--ink-light);
    overflow: hidden;
  }
  .label--front { left: 92px; }
  .label--back { left: 638px; }

  /* Front label */
  .front__wash {
    position: absolute;
    left: 0; top: 200px;
    width: 470px; height: 270px;
    background: radial-gradient(ellipse 60% 55% at 40% 50%, rgba(94,14,18,0.55), rgba(94,14,18,0) 75%);
  }
  .brand {
    position: absolute;
    left: 0; right: 0; top: 50px;
    display: flex; flex-direction: column; align-items: center;
  }
  .brand__mark {
    width: 84px; height: 84px;
    border: 3px solid var(--ink-light);
    border-radius: 50%;
  }
  .brand__name {
    margin-top: 62px;
    font-family: "DM Serif Display", serif;
    font-size: 25px;
    letter-spacing: 0.5px;
    text-transform: uppercase;
  }
  .wine-name {
    position: absolute;
    left: 0; right: 0; top: 300px;
    text-align: center;
    font-family: "DM Serif Display", serif;
    font-size: 70px;
    line-height: 1;
    letter-spacing: 1px;
  }
  .blend {
    position: absolute;
    left: 0; right: 0; top: 384px;
    text-align: center;
    font-family: "Playfair Display", serif;
    font-weight: 700;
    font-size: 21px;
  }
  .blend__divider { margin: 0 10px; font-weight: 400; }
  .vintage {
    position: absolute;
    left: 0; right: 0; top: 500px;
    text-align: center;
    font-family: "Playfair Display", serif;
    font-size: 40px;
    line-height: 1;
  }
  .origin {
    position: absolute;
    left: 0; right: 0; top: 556px;
    text-align: center;
    font-family: "Playfair Display", serif;
    font-size: 19px;
    letter-spacing: 1.5px;
  }

  /* Back label */
  .tagline {
    position: absolute;
    left: 0; right: 0; top: 38px;
    text-align: center;
    font-family: "Pinyon Script", cursive;
    font-weight: 400;
    font-size: 30px;
  }
  .story {
    position: absolute;
    left: 28px; right: 24px; top: 90px;
    text-align: center;
    font-family: "Playfair Display", serif;
    font-size: 19.5px;
    line-height: 26.3px;
  }
  .signoff {
    position: absolute;
    left: 0; right: 0; top: 290px;
    text-align: center;
    font-family: "Pinyon Script", cursive;
    font-size: 21px;
    line-height: 27px;
  }
  .signoff__rule {
    position: absolute;
    left: 155px; top: 352px;
    width: 150px; height: 1px;
    background: linear-gradient(90deg, rgba(255,255,255,0), rgba(42,7,8,0.7), rgba(255,255,255,0));
  }
  .warning {
    position: absolute;
    left: 31px; right: 24px; top: 370px;
    font-family: "Open Sans", sans-serif;
    font-weight: 300;
    font-size: 17px;
    line-height: 24px;
    text-align: justify;
  }
  .warning strong { font-weight: 600; }
  .producer {
    position: absolute;
    left: 31px; top: 516px;
    width: 220px;
    font-family: "Open Sans", sans-serif;
    font-size: 17.5px;
    line-height: 24px;
    white-space: nowrap;
  }
  .disclosure {
    position: absolute;
    right: 45px; top: 531px;
    width: 170px;
    text-align: center;
    font-family: "Open Sans", sans-serif;
    font-weight: 300;
    font-size: 13.5px;
    line-height: 17px;
    text-transform: uppercase;
  }
  .volume {
    position: absolute;
    right: 22px; top: 584px;
    font-family: "Open Sans", sans-serif;
    font-weight: 700;
    font-size: 21px;
    line-height: 26px;
    color: var(--ink-dark);
    white-space: nowrap;
  }
  .volume__size { margin-left: 14px; }
</style>
</head>
<body>
  <section class="label label--front" aria-label="Front label">
    <div class="front__wash" role="img" aria-label="Soft dark red watercolour wash behind the wine name"></div>
    <div class="brand">
      <div class="brand__mark"></div>
      <div class="brand__name">QT Hollowpath Wine</div>
    </div>
    <h1 class="wine-name">K&amp;W RED</h1>
    <p class="blend">40% Barbera<span class="blend__divider">|</span>60% Sangiovese</p>
    <p class="vintage">2019</p>
    <p class="origin">SORREL FLATS, ARIZONA</p>
  </section>

  <section class="label label--back" aria-label="Back label">
    <h2 class="tagline">Our Mission is Your Enjoyment!</h2>
    <p class="story">Produced from grapes grown at a 4,300 foot elevation, these Italian varietals thrive in sandy loam, replete with nutrients and are brought to our Mesa Kinfolk Vineyard by Juniper Creek. Further nourishment by the monsoon climate of the high Arizona desert produces this wine’s unique characteristics.</p>
    <p class="signoff">Salud!<br>Juna &amp; Orrin</p>
    <div class="signoff__rule"></div>
    <p class="warning"><strong>Government warning:</strong> (1) according to the surgeon general, women should not drink alcoholic beverages during pregnancy because of the risk of birth defects. (2) consumption of alcoholic beverages impairs your ability to drive a car or operate machinery, and may cause health problems.</p>
    <p class="producer">Produced and bottled by<br>Dravenmoor Wine Company<br>Sorrel Flats, Arizona&nbsp; 85999<br>qthwine@mail.example</p>
    <p class="disclosure">130 cases produced<br>contains sulfites</p>
    <p class="volume"><span class="volume__abv">13.5% vol.</span><span class="volume__size">750 ml</span></p>
  </section>
</body>
</html>
```